Business Card + Stationery Design for a Craft Beer Bar

Mr. Tolvek's is a taproom sport bar that contains in its menu beers from different places around the world. What we offer differently is the experience that you can get inside our location, ambient music with rock from the 80s to 90s, projection with the sports of the moment, board games and private events.

Target Market(s)

Young people, Mid and High Class

Industry/Entity Type

Business

Font styles to use
Serif
Sans Serif

Colors
fee18a

Requirements
Must have
• Name, Title, Contact Details, Website
Nice to have
• Mail Signature
Should not have
• n/a

```html
<!DOCTYPE html>
<html lang="en">
<head>
<meta charset="utf-8">
<title>Mr. Tolvek's Taproom – Business Card</title>
<link rel="stylesheet" href="https://fonts.googleapis.com/css2?family=Oswald:wght@500&family=Open+Sans:wght@400;600&display=swap">
<style>
  :root {
    --backdrop: #d9d9d9;
    --card-yellow: #f4c25a;
    --card-black: #1c1c1c;
    --ink-black: #111111;
    --gold: #d9a73c;
    --white: #ffffff;
    --muted-white: #e8e8e8;
  }
  * { margin: 0; padding: 0; box-sizing: border-box; }
  html, body {
    width: 1200px; height: 900px; overflow: hidden;
    background: var(--backdrop);
  }
  .canvas { position: relative; width: 1200px; height: 900px; }
  .card {
    position: absolute; left: 250px; width: 700px; height: 400px;
    box-shadow: 0 6px 18px rgba(0,0,0,0.18);
  }
  .card--front { top: 30px; background: var(--card-yellow); }
  .card--back  { top: 470px; background: var(--card-black); }

  .front-name {
    position: absolute; left: 110px; top: 170px;
    font-family: "Open Sans", sans-serif; font-weight: 600;
    font-size: 40px; line-height: 1; color: var(--ink-black);
  }

  .holder {
    position: absolute; left: 50px; top: 120px;
    font-family: "Oswald", sans-serif; font-weight: 500;
  }
  .holder__name { color: var(--gold); font-size: 30px; letter-spacing: 0.5px; line-height: 1.1; }
  .holder__title { color: var(--muted-white); font-size: 17px; letter-spacing: 0.5px; }

  .divider {
    position: absolute; left: 250px; right: 40px; top: 185px;
    height: 1px; background: var(--gold);
  }

  .back-name {
    position: absolute; right: 40px; top: 128px;
    font-family: "Open Sans", sans-serif; font-weight: 600;
    font-size: 26px; line-height: 1; color: var(--white);
  }

  .contacts {
    position: absolute; right: 40px; top: 230px;
    list-style: none;
    font-family: "Open Sans", sans-serif; font-size: 21px;
    color: var(--white); text-align: right;
  }
  .contacts__item {
    display: flex; justify-content: flex-end; align-items: center;
    gap: 12px; line-height: 30px;
  }
  .contacts__icon { width: 16px; height: 16px; flex: none; }
  .contacts__icon * { fill: none; stroke: var(--gold); stroke-width: 1.6; stroke-linecap: round; stroke-linejoin: round; }
</style>
</head>
<body>
<main class="canvas">

  <section class="card card--front" aria-label="Business card front">
    <p class="front-name">Mr. Tolvek's Taproom</p>
  </section>

  <section class="card card--back" aria-label="Business card back">
    <div class="holder">
      <div class="holder__name">MARCUS HALE</div>
      <div class="holder__title">MANAGING DIRECTOR</div>
    </div>
    <div class="divider"></div>

    <p class="back-name">Mr. Tolvek's Taproom</p>

    <ul class="contacts">
      <li class="contacts__item">123.456.7890
        <svg class="contacts__icon" viewBox="0 0 16 16"><rect x="4" y="1" width="8" height="14" rx="1.5"/><line x1="7" y1="12.5" x2="9" y2="12.5"/></svg>
      </li>
      <li class="contacts__item">123.456.7890
        <svg class="contacts__icon" viewBox="0 0 16 16"><path d="M2 6c0-2 3-3 6-3s6 1 6 3l-2 1-2-1V5H6v1L4 7z"/><rect x="3" y="9" width="10" height="5" rx="1"/></svg>
      </li>
      <li class="contacts__item">info@youremail.com
        <svg class="contacts__icon" viewBox="0 0 16 16"><rect x="1.5" y="3.5" width="13" height="9" rx="1"/><path d="M1.5 4l6.5 5 6.5-5"/></svg>
      </li>
      <li class="contacts__item">www.website.com
        <svg class="contacts__icon" viewBox="0 0 16 16"><path d="M7 9l2-2"/><path d="M6 7L4 9a2.1 2.1 0 003 3l2-2"/><path d="M10 9l2-2a2.1 2.1 0 00-3-3L7 6"/></svg>
      </li>
    </ul>
  </section>

</main>
</body>
</html>
```